Etiketten-Design für familiengeführten Weinbaubetrieb
Zielgruppe
Wir sind ein Familiengeführter Weinbaubetrieb und vermarkten unseren Wein in 0,75l Flaschen sowie auch Säfte und Schnäpse.
Zur zeit Verkaufen wir unseren Wein an Gastro und Private Kunden auch teils über Messen
Aufgabenstellung
Das derzeitige Etikett ist recht schlicht gestaltet und das Logo besteht rein aus dem geschriebenen Namen Winzerhof Dolmeck. Es kann aber auch gerne nur mit dem Namen Dolmeck ohne Winzerhof gearbeitet werden! Mit dem einbringen einer neuen Generation in den Betrieb wollen wir das aussehen unserer Produkte erneuern. Dazu kann sich gerne mit dem Namen als 'Logo' in jeglicher Art gespielt werden. Wir füllen unsere Weine in 0,75l Bordeaux Flaschen. Die Form des Etikett ist kein K.O. Kriterium jedoch wurde ursprünglich ein rund um Etikett angedacht. Sollten die Designes sich auch anders realisieren lassen sind wir gerne offen für Ideen.

```html
<!DOCTYPE html>
<html lang="de">
<head>
<meta charset="utf-8">
<title>Dolmeck – Weinetiketten</title>
<link rel="stylesheet" href="https://fonts.googleapis.com/css2?family=Roboto+Slab:wght@300;600&display=swap">
<style>
  :root {
    --canvas: #ffffff;
    --label: #f5f5f5;
    --label-edge: #e6e6e6;
    --white-wine: #a9a21a;
    --white-wine-deep: #b3a81e;
    --white-splash: #e6e2b8;
    --red-wine: #3a1014;
    --red-wine-deep: #3e1418;
    --red-splash: #d8ccd0;
  }
  * { box-sizing: border-box; margin: 0; padding: 0; }
  html, body {
    width: 1200px; height: 1200px; overflow: hidden;
    background: var(--canvas);
  }
  .label-set {
    width: 1200px; height: 1200px;
    display: flex; align-items: center; justify-content: center;
    gap: 30px;
  }
  .label {
    position: relative;
    width: 260px; height: 216px;
    background: var(--label);
    border: 1px solid var(--label-edge);
    font-family: "Roboto Slab", Georgia, serif;
    color: var(--ink);
    display: flex; flex-direction: column; align-items: center;
    overflow: hidden;
  }
  .label--white-a { --ink: var(--white-wine); --splash: var(--white-splash); }
  .label--white-b { --ink: var(--white-wine-deep); --splash: var(--white-splash); }
  .label--red-a { --ink: var(--red-wine); --splash: var(--red-splash); }
  .label--red-b { --ink: var(--red-wine-deep); --splash: var(--red-splash); }

  .label__splash {
    position: absolute;
    left: 88px; top: 8px;
    width: 130px; height: 200px;
    background: radial-gradient(ellipse at 45% 55%, var(--splash) 0%, rgba(255,255,255,0) 68%);
    opacity: 0.9;
  }
  .label__mark {
    position: relative;
    margin-top: 14px;
    width: 34px; height: 34px;
    border: 1.5px solid var(--ink);
    border-radius: 50%;
  }
  .label__house {
    position: relative;
    margin-top: 6px;
    font-size: 14px; font-weight: 600;
    letter-spacing: 0.14em;
    text-transform: uppercase;
  }
  .label__variety {
    position: relative;
    margin-top: 14px;
    font-size: 35px; font-weight: 300;
    line-height: 1.08;
    letter-spacing: 0.06em;
    text-align: center;
    text-transform: uppercase;
  }
  .label__vintage {
    position: relative;
    margin-top: 14px;
    font-size: 11px; font-weight: 300;
    letter-spacing: 0.22em;
  }
</style>
</head>
<body>
  <main class="label-set">
    <article class="label label--white-a">
      <div class="label__splash" role="img" aria-label="Pinselspritzer in hellem Weißweinton"></div>
      <span class="label__mark"></span>
      <span class="label__house">Dolmeck</span>
      <h2 class="label__variety">Wein<br>Sorte</h2>
      <span class="label__vintage">2023</span>
    </article>
    <article class="label label--white-b">
      <div class="label__splash" role="img" aria-label="Pinselspritzer in hellem Weißweinton"></div>
      <span class="label__mark"></span>
      <span class="label__house">Dolmeck</span>
      <h2 class="label__variety">Wein<br>Sorte</h2>
      <span class="label__vintage">2023</span>
    </article>
    <article class="label label--red-a">
      <div class="label__splash" role="img" aria-label="Pinselspritzer in zartem Rotweinton"></div>
      <span class="label__mark"></span>
      <span class="label__house">Dolmeck</span>
      <h2 class="label__variety">Wein<br>Sorte</h2>
      <span class="label__vintage">2023</span>
    </article>
    <article class="label label--red-b">
      <div class="label__splash" role="img" aria-label="Pinselspritzer in zartem Rotweinton"></div>
      <span class="label__mark"></span>
      <span class="label__house">Dolmeck</span>
      <h2 class="label__variety">Wein<br>Sorte</h2>
      <span class="label__vintage">2023</span>
    </article>
  </main>
</body>
</html>
```